Design a New Business Card for Our Company

We are looking for fresh, unique, and a modern business card that reflects our roots as digital marketing agency focused on SEM.

Industry/Entity Type

Marketing

Contact Information for Business Card

looking for very unique out of the box designs. clean and modern that compliments our logo

Requirements
Must have
• colors should match our logo
• Front should have name, address, email, and phone/fax of the person, phone/fax are the same number
• back should have our url

```html
<!DOCTYPE html>
<html lang="en">
<head>
<meta charset="utf-8">
<title>Brightpath Media – Business Card</title>
<link rel="stylesheet" href="https://fonts.googleapis.com/css2?family=Questrial&display=swap">
<style>
  :root {
    --backdrop: #1a1a1a;
    --card-blue: #5e98d0;
    --accent-blue: #4f8fd6;
    --silver-light: #dcdcdc;
    --silver-dark: #a8a8a8;
    --ink-white: #ffffff;
    --faint-mark: rgba(150, 170, 200, 0.35);
  }
  * { box-sizing: border-box; margin: 0; padding: 0; }
  html, body {
    width: 1200px;
    height: 800px;
    overflow: hidden;
    background: var(--backdrop);
    font-family: "Questrial", "Century Gothic", sans-serif;
  }
  .canvas {
    position: relative;
    width: 1200px;
    height: 800px;
    display: flex;
    align-items: center;
    justify-content: center;
    gap: 60px;
  }
  .card {
    position: relative;
    width: 520px;
    height: 300px;
    overflow: hidden;
  }

  /* Front: contact side */
  .card-front {
    background: linear-gradient(160deg, var(--silver-light) 0%, #c4c4c4 55%, var(--silver-dark) 100%);
  }
  .person-name {
    position: absolute;
    left: 34px;
    top: 34px;
    font-size: 20px;
    color: var(--accent-blue);
  }
  .person-title {
    position: absolute;
    left: 34px;
    top: 60px;
    font-size: 12px;
    color: var(--ink-white);
  }
  .divider {
    position: absolute;
    left: 30px;
    right: 30px;
    top: 82px;
    height: 2px;
    background: var(--accent-blue);
  }
  .contact-list {
    position: absolute;
    left: 34px;
    top: 104px;
    list-style: none;
    font-size: 13px;
    line-height: 20px;
    color: var(--ink-white);
  }
  .front-brand {
    position: absolute;
    right: 34px;
    top: 34px;
    display: flex;
    align-items: center;
    gap: 8px;
    font-size: 26px;
    color: var(--ink-white);
  }
  .front-brand .brand-dot {
    width: 18px;
    height: 18px;
    border-radius: 50%;
    background: var(--ink-white);
  }
  .corner-mark {
    position: absolute;
    right: 36px;
    bottom: 24px;
    width: 110px;
    height: 110px;
    border-radius: 50%;
    background: var(--faint-mark);
  }

  /* Back: brand side */
  .card-back {
    background: var(--card-blue);
    display: flex;
    flex-direction: column;
    align-items: center;
    justify-content: center;
    gap: 14px;
  }
  .back-brand {
    display: flex;
    align-items: center;
    gap: 14px;
    font-size: 46px;
    color: var(--ink-white);
  }
  .back-brand .brand-dot {
    width: 36px;
    height: 36px;
    border-radius: 50%;
    background: var(--ink-white);
  }
  .back-url {
    font-size: 14px;
    letter-spacing: 3px;
    color: var(--ink-white);
  }
</style>
</head>
<body>
  <main class="canvas">
    <section class="card card-front" aria-label="Business card front">
      <h1 class="person-name">Your Name goes here</h1>
      <p class="person-title">Your Title</p>
      <div class="divider"></div>
      <ul class="contact-list">
        <li>Your Address goes here</li>
        <li>p: 0123456789</li>
        <li>f : 0123456789</li>
        <li>e: yourname@brightpathmedia.com</li>
        <li>w: www.brightpathmedia.com</li>
      </ul>
      <div class="front-brand"><span class="brand-dot"></span>Brightpath Media</div>
      <div class="corner-mark"></div>
    </section>

    <section class="card card-back" aria-label="Business card back">
      <div class="back-brand"><span class="brand-dot"></span>Brightpath Media</div>
      <p class="back-url">www.brightpathmedia.com</p>
    </section>
  </main>
</body>
</html>
```